Report Cover

This is for a Binder Front, Side, Back. I have uploaded a few examples. We are an education resource company that delivers data in a format that allows districts to make better decisions. Our color palette is uploaded as well.

```html
<!DOCTYPE html>
<html lang="en">
<head>
<meta charset="utf-8">
<title>Larkmoor School District 2024 – Comprehensive Needs Assessment</title>
<link href="https://fonts.googleapis.com/css2?family=Poppins:wght@700&family=Barlow:wght@400;500&family=Barlow+Condensed:wght@400;500&display=swap" rel="stylesheet">
<style>
  :root {
    --navy: #2b2e6e;
    --pink: #e8405e;
    --coral: #f06d63;
    --teal: #5fc5b3;
    --yellow: #fcc85a;
    --taupe: #a99c91;
    --slate: #4b4d79;
    --ink: #1e1e24;
    --brand-grey: #3a3a3a;
    --brand-green: #8cc63f;
    --paper-top: #ffffff;
    --paper-mid: #f2f2f3;
    --paper-bottom: #e6e6e8;
  }
  * { margin: 0; padding: 0; box-sizing: border-box; }
  html, body { width: 927px; height: 1200px; overflow: hidden; background: #ffffff; }
  .cover {
    position: relative;
    width: 927px;
    height: 1200px;
    overflow: hidden;
    background: var(--paper-top);
  }
  .cover__texture {
    position: absolute;
    left: 0; top: 520px;
    width: 927px; height: 680px;
    background: linear-gradient(180deg, var(--paper-top) 0%, var(--paper-mid) 35%, var(--paper-bottom) 100%);
  }
  .cover__band {
    position: absolute;
    left: 0; top: 0;
    width: 927px; height: 1200px;
  }
  .cover__pattern {
    position: absolute;
    left: 382px; top: 390px;
    width: 545px; height: 330px;
    background: linear-gradient(135deg, var(--yellow) 0%, var(--teal) 35%, var(--slate) 55%, var(--taupe) 70%, var(--coral) 85%, var(--yellow) 100%);
    opacity: 0.85;
  }
  .cover__pattern-corner {
    position: absolute;
    left: 862px; top: 288px;
    width: 65px; height: 102px;
    background: linear-gradient(180deg, var(--yellow) 0%, var(--teal) 100%);
    opacity: 0.85;
  }
  .title {
    position: absolute;
    line-height: 1;
    text-align: right;
    white-space: nowrap;
  }
  .title--client {
    top: 72px;
    right: 70px;
    font-family: "Poppins", sans-serif;
    font-weight: 700;
    font-size: 102px;
    letter-spacing: 5px;
    color: var(--navy);
  }
  .title--district {
    top: 200px;
    right: 90px;
    font-family: "Barlow", sans-serif;
    font-weight: 400;
    font-size: 91px;
    letter-spacing: 3px;
    color: var(--pink);
  }
  .title--year {
    top: 272px;
    right: 78px;
    font-family: "Barlow Condensed", sans-serif;
    font-weight: 500;
    font-size: 124px;
    color: var(--navy);
  }
  .brand {
    position: absolute;
    left: 648px;
    top: 728px;
    display: flex;
    align-items: center;
    gap: 10px;
  }
  .brand__dot {
    width: 24px; height: 24px;
    border-radius: 50%;
    background: var(--brand-green);
  }
  .brand__name {
    font-family: "Barlow", sans-serif;
    font-weight: 500;
    font-size: 30px;
    line-height: 1.05;
    color: var(--brand-grey);
  }
  .report-type {
    position: absolute;
    left: 0; width: 927px;
    text-align: center;
    line-height: 1;
    white-space: nowrap;
    font-family: "Barlow Condensed", sans-serif;
    font-weight: 500;
  }
  .report-type__main {
    top: 966px;
    font-size: 72px;
    color: var(--navy);
  }
  .report-type__sub {
    top: 1060px;
    font-size: 56px;
    color: var(--ink);
  }
</style>
</head>
<body>
<main class="cover">
  <div class="cover__texture" role="img" aria-label="Soft light grey background with a faint diamond tile texture"></div>

  <svg class="cover__band" viewBox="0 0 927 1200" aria-hidden="true">
    <polygon points="0,495 523,606 421,718 0,601" fill="var(--coral)"/>
  </svg>

  <div class="cover__pattern" role="img" aria-label="Decorative cluster of coloured triangles in yellow, teal, slate, taupe and coral"></div>
  <div class="cover__pattern-corner" role="img" aria-label="Decorative triangles in yellow and teal at the page edge"></div>

  <h1 class="title title--client">LARKMOOR</h1>
  <p class="title title--district">SCHOOL DISTRICT</p>
  <p class="title title--year">2024</p>

  <div class="brand">
    <span class="brand__dot"></span>
    <span class="brand__name">Clearpath<br>Learning, LLC</span>
  </div>

  <h2 class="report-type report-type__main">COMPREHENSIVE</h2>
  <p class="report-type report-type__sub">NEEDS ASSESSMENT</p>
</main>
</body>
</html>
```